Large corporation needs landing page for its employees with emotional and psychological problems

Vision:
Hello, we are a startup and would like to build a landing page and website in the mental health sector for a large corporation. In this site employees with emotional and psychological problems should quickly receive professional psychological support. This support takes the form of internal referrals from employees who are looking for help to qualified therapists, so that help can be provided quickly.
Furthermore, the employees get access to a tool where they can find out about topics in the mind health area and can also get help via webinars and podcasts. The employee should thus be able to take the hurdle to seek help and support in good time.
Therapists for whom the focus is on the urgency of providing quick help and support will work here in cooperation with the respective corporations.
Keywords:
• Help/Support
• overcome inhibitions
• Competent help
• Uncomplicated help
• Permanent access
• protected space
• Recognizing and naming emotional problems and actively tackling them
• get help
• mindfulness
• everyday helper
• Informative
• Anonymous
• compassion
• tolerance
• respect
• Appreciation
• empathy
• mindfulness
• protected space
• To be needed
• Like a lighthouse signal
What we need:
Landingpage
We need a landing page aimed at getting employees to contact psychological help. The call to action is to get in contact via a contact form.
Landing page content
There are several text modules:
• A heading/greeting
• A body of text at the beginning that explains the purpose of the page
• A bulleted text area describing the pain points and the solutions to them
Video:
The heart of the content will be a video explaining the need and inviting them to get in touch.
contact form:
It should be kept simple: first name, last name and email address
Legally required content:
General terms and conditions, data protection and imprint. These are only given as links in the footer.
In parallel, the Corporate Design should be adapted/extended:
Logo:
The font in the logo should be revised. The wings in the background remain.
Please adapt the logo for different uses:
• on a black background
• with transparent background
• favorite icon (browser)
• In square format for social media
Colors:
• develop a color chart based on the colors of the logo.
• please determine 2-3 main colors and the matching variations. I.e. transparent variations or light colors.
Typography:
Determine a decorative font and/or typography for headings and a text font. There should be no more than 3 fonts.
Industry/Entity Type
to recruit therapists as employees
Requirements
Should not have
- please not to playful design or typography - and max. 3 colors

```html
<!DOCTYPE html>
<html lang="en">
<head>
<meta charset="utf-8">
<title>Calm Harbor – Professional Psychological Support</title>
<link href="https://fonts.googleapis.com/css2?family=Inter:wght@400;500;600;700&family=Rubik:wght@500;600;700&display=swap" rel="stylesheet">
<style>
:root{
  --teal:#0b5263;
  --teal-light:#5aaec3;
  --ink:#1d1f2b;
  --text:#2e3440;
  --wave-1:#c6e1e9;
  --wave-2:#deeff3;
  --white:#ffffff;
  --footer:#1f2030;
  --footer-text:#b8bcc6;
}
*{box-sizing:border-box;margin:0;padding:0}
html,body{width:1200px;height:4970px;overflow:hidden}
body{position:relative;background:var(--white);font-family:"Inter",sans-serif;color:var(--text)}
.abs{position:absolute}
h1,h2,h3{font-family:"Rubik",sans-serif}

/* header */
.brand{left:98px;top:20px;font-weight:600;font-size:38px;color:var(--teal);letter-spacing:-0.5px;z-index:3}
.social{display:flex;gap:8px}
.social span{display:block;width:30px;height:30px;border:2px solid var(--teal);border-radius:5px;background:rgba(255,255,255,.85)}
.header-social{left:796px;top:24px;z-index:3}
.phone{left:936px;top:22px;width:164px;height:38px;background:var(--teal);border-radius:19px 4px 4px 19px;display:flex;align-items:center;gap:10px;padding-left:4px;color:#fff;font-weight:600;font-size:16px;z-index:3}
.phone i{width:30px;height:30px;border-radius:50%;background:#fff;display:flex;align-items:center;justify-content:center}

/* hero */
.hero-photo{left:0;top:0;width:1200px;height:880px;background:linear-gradient(120deg,#d9dfe3 0%,#b9c4cc 30%,#8b969d 55%,#6f7a80 75%,#9aa5ab 100%)}
.hero-waves{left:0;top:620px;width:1200px;height:350px;background:linear-gradient(180deg,rgba(222,239,243,0) 0%,rgba(198,225,233,.9) 35%,var(--wave-2) 60%,var(--white) 100%);z-index:2}
.hero-title{left:102px;top:470px;font-weight:700;font-size:48px;line-height:54px;color:#fff;z-index:3}
.form{left:720px;top:116px;width:376px;height:448px;background:var(--teal);border-radius:4px;padding:24px 28px;color:#fff;z-index:3}
.form h2{font-size:33px;font-weight:600;margin-bottom:16px}
.form label{display:block;font-size:15px;font-weight:600;margin-bottom:8px}
.form .field{height:44px;background:#fff;border-radius:3px;margin-bottom:24px;font-size:14px;color:#8a8f98;padding:0 8px;display:flex;align-items:center}
.form .submit{width:136px;height:44px;border:2px solid #fff;border-radius:4px;display:flex;align-items:center;justify-content:center;font-weight:600;font-size:16px;margin-left:4px;margin-top:-4px}

/* about */
.eyebrow{left:98px;top:1017px;font-size:14px;font-weight:700;color:var(--teal);letter-spacing:.5px}
.about-title{left:98px;top:1035px;font-size:54px;font-weight:700;color:var(--teal)}
.about-text{left:98px;top:1120px;width:495px;font-size:15px;line-height:26.6px}
.photo{border-radius:18px}
.about-photo{left:642px;top:1023px;width:453px;height:348px;background:linear-gradient(135deg,#e9ecef,#cfd3d4 45%,#a99d88 75%,#d8d2c6)}

/* offer */
.offer{left:0;top:1432px;width:1200px;height:830px;background:var(--teal)}
.offer-title{left:0;top:1500px;width:1200px;text-align:center;font-size:52px;font-weight:600;color:#fff}
.offer-sub{left:190px;top:1567px;width:820px;text-align:center;font-size:15.5px;line-height:26px;color:#fff}
.service{width:330px;text-align:center;color:#fff}
.service .icon{width:96px;height:96px;margin:0 auto 18px;border-radius:14px;background:rgba(255,255,255,.14)}
.service h3{font-family:"Inter",sans-serif;font-size:18px;font-weight:600;margin-bottom:10px}
.service p{width:316px;margin:0 auto;font-size:15.5px;line-height:26px}

/* who */
.who-title{left:98px;top:2376px;font-size:52px;font-weight:700;color:var(--ink)}
.who-text{left:98px;top:2448px;width:490px;font-size:15.5px;line-height:26.5px}
.who-photo{left:612px;top:2386px;width:486px;height:356px;background:linear-gradient(120deg,#eceeed,#d7dad5 40%,#b8bdb3 70%,#e3e4e1)}
.stats{left:98px;top:2592px;width:540px;height:110px;background:#fff;border-radius:6px;box-shadow:0 6px 24px rgba(0,0,0,.1);display:flex;z-index:2}
.stat{flex:1;text-align:center;padding-top:18px;border-right:1px solid #e5e7eb}
.stat:last-child{border-right:none}
.stat b{display:block;font-weight:500;font-size:42px;color:var(--teal);line-height:46px}
.stat span{font-size:14px}

/* video */
.video{left:100px;top:2868px;width:996px;height:498px;border-radius:14px;background:linear-gradient(180deg,#8fa8a8 0%,#b4bfae 45%,#c9b888 75%,#a99a73 100%);box-shadow:0 14px 34px rgba(0,0,0,.18)}
.play{left:534px;top:3058px}
.share{left:1048px;top:2884px}

/* benefits */
.benefits-title{left:98px;top:3532px;font-size:52px;font-weight:700;line-height:58px;color:var(--ink)}
.benefits-title em{font-style:normal;color:var(--teal)}
.benefits{left:98px;top:3673px;width:470px;list-style:none;font-size:15.5px;font-weight:600;line-height:26px;color:var(--ink)}
.benefits li{position:relative;padding-left:18px;margin-bottom:9px}
.benefits li::before{content:"";position:absolute;left:0;top:9px;width:8px;height:8px;border-radius:50%;background:var(--teal)}
.benefits-photo{left:612px;top:3509px;width:486px;height:356px;background:linear-gradient(135deg,#e6e9ea,#c7ccce 45%,#4b5560 75%,#d9dcdb)}

/* testimonial */
.testimonial-photo{left:100px;top:3942px;width:455px;height:484px;background:linear-gradient(135deg,#eae7df,#b7ad9a 45%,#6b6555 75%,#9b9486)}
.footer-waves{left:0;top:4360px;width:1200px;height:300px;background:linear-gradient(180deg,rgba(255,255,255,0) 0%,var(--wave-2) 25%,var(--wave-1) 50%,#6f8f9c 75%,var(--footer) 100%);z-index:2}
.quote-card{left:482px;top:3999px;width:614px;height:374px;background:#fff;border-radius:18px;box-shadow:0 8px 30px rgba(0,0,0,.08);padding:34px 34px 0;z-index:3}
.quote-card h2{font-family:"Inter",sans-serif;font-weight:400;font-size:40px;color:var(--ink);margin:14px 0 10px}
.quote-card p{font-size:20px;line-height:29px;color:var(--ink)}
.person{display:flex;align-items:center;gap:14px;margin-top:24px}
.avatar{width:68px;height:68px;border-radius:50%;background:linear-gradient(135deg,#c9d3e8,#8c93b8)}
.person b{display:block;color:var(--teal);font-size:19px;font-weight:600}
.person span{font-size:13px}
.arrow-l{left:490px;top:4176px;z-index:4}
.arrow-r{left:1068px;top:4176px;z-index:4}

/* footer */
.footer{left:0;top:4660px;width:1200px;height:310px;background:var(--footer)}
.footer-brand{left:98px;top:4686px;font-size:44px;font-weight:600;color:var(--teal-light);z-index:3}
.footer-social{left:160px;top:4766px;z-index:3}
.footer-social span{width:46px;height:46px;border-color:#fff;background:transparent}
.footer-heading{font-size:20px;font-weight:600;color:var(--teal-light);z-index:3}
.links{left:517px;top:4740px;list-style:none;font-size:15px;color:var(--footer-text);z-index:3}
.links li{margin-bottom:24px}
.links li::before{content:"›";margin-right:10px;color:#fff}
.footer-about{left:806px;top:4732px;width:296px;font-size:15px;line-height:26.5px;color:var(--footer-text);z-index:3}
.rule{left:98px;top:4894px;width:1004px;height:1px;background:#3a3c4d;z-index:3}
.copyright{left:98px;top:4922px;font-size:14px;color:#9aa0ab;z-index:3}
.copyright b{color:#fff;font-weight:500}
</style>
</head>
<body>

<!-- hero -->
<div class="abs hero-photo" role="img" aria-label="Photo of a young woman talking with a therapist on a sofa in a bright office"></div>
<div class="abs hero-waves" role="img" aria-label="Decorative light blue wave bands"></div>
<div class="abs brand">calm harbor</div>
<div class="abs social header-social" aria-label="Social links"><span></span><span></span><span></span></div>
<div class="abs phone"><i><svg width="16" height="16" viewBox="0 0 24 24"><path fill="#0b5263" d="M6.6 10.8a15.1 15.1 0 0 0 6.6 6.6l2.2-2.2c.3-.3.7-.4 1-.2 1.1.4 2.3.6 3.6.6.6 0 1 .4 1 1V20c0 .6-.4 1-1 1A17 17 0 0 1 3 4c0-.6.4-1 1-1h3.5c.6 0 1 .4 1 1 0 1.3.2 2.5.6 3.6.1.3 0 .7-.2 1z"/></svg></i>1800 555 010</div>
<h1 class="abs hero-title">Professional<br>Psychological Support</h1>
<form class="abs form">
  <h2>How Can We Help?</h2>
  <label>First Name</label><div class="field">Type First Name</div>
  <label>Last Name</label><div class="field">Type Last Name</div>
  <label>Email Address</label><div class="field">Enter email address</div>
  <div class="submit">Submit</div>
</form>

<!-- about -->
<div class="abs eyebrow">ABOUT</div>
<h2 class="abs about-title">Calm Harbor</h2>
<p class="abs about-text">Lorem ipsum dolor sit amet, consectetur adipiscing elit. Phasellus pretium metus sem, convallis laoreet lorem viverra id. Donec vitae pellenque leo, et feugiat lacus. Fusce vulputate, quam vitae sollicitudin facilisis, urna nisi porttitor neque, vel euismod orci massa ac enim. Curabitur ultrices a libero nec suscipit. Integer tortor dolor, tincidunt non ipsum at, blandit interdum magna. Phasellus ac lorem condimentum, efficitur metus vitae, porta est. Fusce massa quam, porttitor vel tortor non, porttitor ullamcorper ex.</p>
<div class="abs photo about-photo" role="img" aria-label="Photo of a therapist taking notes while a client relaxes on a chair"></div>

<!-- offer -->
<section class="abs offer"></section>
<h2 class="abs offer-title">What We Can Offer</h2>
<p class="abs offer-sub">Vestibulum ante ipsum primis in faucibus orci luctus et ultrices posuere cubilia curae; Quisque in commodo odio, eu ultrices mi. Sed auctor ante mollis, viverra purus sit amet, iaculis eros.</p>
<div class="abs service" style="left:92px;top:1690px"><div class="icon" role="img" aria-label="Line icon of a head with a heart"></div><h3>Relationship</h3><p>Lorem ipsum dolor sit amet, consectetur adipiscing elit. Morbi dictum tempus urna, cursus ac</p></div>
<div class="abs service" style="left:435px;top:1690px"><div class="icon" role="img" aria-label="Line icon of a person sitting with head down"></div><h3>Depression</h3><p>Lorem ipsum dolor sit amet, consectetur adipiscing elit. Morbi dictum tempus urna, cursus ac</p></div>
<div class="abs service" style="left:779px;top:1690px"><div class="icon" role="img" aria-label="Line icon of puzzle pieces"></div><h3>Mind Game</h3><p>Lorem ipsum dolor sit amet, consectetur adipiscing elit. Morbi dictum tempus urna, cursus ac</p></div>
<div class="abs service" style="left:92px;top:1966px"><div class="icon" role="img" aria-label="Line icon of two clashing hands"></div><h3>Conflicting</h3><p>Lorem ipsum dolor sit amet, consectetur adipiscing elit. Morbi dictum tempus urna, cursus ac</p></div>
<div class="abs service" style="left:435px;top:1966px"><div class="icon" role="img" aria-label="Line icon of a head with a heart-shaped brain"></div><h3>Mental Health</h3><p>Lorem ipsum dolor sit amet, consectetur adipiscing elit. Morbi dictum tempus urna, cursus ac</p></div>
<div class="abs service" style="left:779px;top:1966px"><div class="icon" role="img" aria-label="Line icon of a lotus flower"></div><h3>Meditation</h3><p>Lorem ipsum dolor sit amet, consectetur adipiscing elit. Morbi dictum tempus urna, cursus ac</p></div>

<!-- who we are -->
<h2 class="abs who-title">Who We Are</h2>
<p class="abs who-text">Curabitur ultrices a libero nec suscipit. Integer t dolor, tincidunt non ipsum at, blandit interdum msellus ac lorem condimentum, efficitur metus vitae, porta est. Cras eros est, iaculis nec nisi sed, hendrerit consequat tellus.</p>
<div class="abs who-photo" role="img" aria-label="Photo of a counsellor listening to a client in a plant-filled room"></div>
<div class="abs stats">
  <div class="stat"><b>14K+</b><span>Happy Clients</span></div>
  <div class="stat"><b>+72%</b><span>Problem Solved</span></div>
  <div class="stat"><b>142+</b><span>Certified Expert</span></div>
</div>

<!-- video -->
<div class="abs video" role="img" aria-label="Video still of a woman sitting peacefully by a lake at sunset"></div>
<svg class="abs play" width="118" height="118" viewBox="0 0 118 118"><circle cx="59" cy="59" r="56" fill="rgba(255,255,255,.12)" stroke="#fff" stroke-width="3"/><path d="M44 34 L86 59 L44 84 Z" fill="#fff"/></svg>
<svg class="abs share" width="38" height="32" viewBox="0 0 24 20"><path fill="#fff" d="M14 0 L24 8 L14 16 V11 C8 11 4 13 1 18 C2 11 6 6 14 5 Z"/></svg>

<!-- benefits -->
<h2 class="abs benefits-title">Benefits of<br><em>Calm Harbor</em></h2>
<ul class="abs benefits">
  <li>Tincidunt non ipsum at, blandit interdum msellus ac</li>
  <li>Lorem condimentum, efficitur metus vitae, porta est.</li>
  <li>Cras eros est, iaculis nec nisi sed, hendrerit consequat tellus.</li>
  <li>Phasellus lacinia quam dolor.</li>
</ul>
<div class="abs benefits-photo" role="img" aria-label="Photo of a therapist with a tablet beside a thoughtful client"></div>

<!-- testimonial -->
<div class="abs photo testimonial-photo" role="img" aria-label="Photo of a group counselling session with people seated in a circle"></div>
<div class="abs footer-waves" role="img" aria-label="Decorative light blue wave bands leading into the footer"></div>
<article class="abs quote-card">
  <svg width="44" height="36" viewBox="0 0 44 36"><path fill="var(--teal)" d="M0 0h18v18c0 10-6 17-15 18v-7c5-1 7-5 7-11H0z M26 0h18v18c0 10-6 17-15 18v-7c5-1 7-5 7-11H26z"/></svg>
  <h2>What they Say</h2>
  <p>Lorem ipsum dolor sit amet, consectetur adipiscing elit. Phasellus pretium metus sem, convallis laoreet lorem viverra id. Donec vitae pellenque leo.</p>
  <div class="person"><div class="avatar" role="img" aria-label="Portrait photo of the client"></div><div><b>Daniel Reed</b><span>Patient</span></div></div>
</article>
<svg class="abs arrow-l" width="16" height="26" viewBox="0 0 16 26"><path d="M13 2 L3 13 L13 24" fill="none" stroke="var(--teal)" stroke-width="3"/></svg>
<svg class="abs arrow-r" width="16" height="26" viewBox="0 0 16 26"><path d="M3 2 L13 13 L3 24" fill="none" stroke="var(--teal)" stroke-width="3"/></svg>

<!-- footer -->
<footer class="abs footer"></footer>
<div class="abs footer-brand">calm harbor</div>
<div class="abs social footer-social"><span></span><span></span><span></span></div>
<h4 class="abs footer-heading" style="left:517px;top:4690px">Useful Links</h4>
<ul class="abs links"><li>Terms and conditions</li><li>Privacy Policy</li></ul>
<h4 class="abs footer-heading" style="left:806px;top:4690px">About Us</h4>
<p class="abs footer-about">Lorem ipsum dolor sit at, consectetur adipiscing elit. Phasellus pretium metus sem, convallis laoreet lorem viverra id. Donec vitae pellenque leo,</p>
<div class="abs rule"></div>
<p class="abs copyright">© 2023 <b>Calm Harbor</b>. All right reserved</p>

</body>
</html>
```